Banner Ad Design Project: Image banner for new website

Hi,

we need an image banner for a new website we just launched. The image banner should come in the formats 728x90 and 300x250.

The website the banner should advertise is http://www.vellora-tonebox.com/ .

We leave it up to your experience to find the best text and to obtain a great clickrate. Banner should be CATCHY and MOTIVATE people to enter. We do not want to include our current "logo". Will require all design files and fonts.

Best regards,
Brendan

```html
<!DOCTYPE html>
<html lang="en">
<head>
<meta charset="utf-8">
<title>Vellora Tonebox – Banner Set</title>
<link rel="stylesheet" href="https://fonts.googleapis.com/css2?family=Cinzel:wght@700&family=EB+Garamond:ital@1&display=swap">
<style>
  :root {
    --stage: #000000;
    --paper: #ffffff;
    --ink: #1d1d1d;
    --ring: #d9d9d9;
    --forest-deep: #5e8a3a;
    --forest-mid: #9dbb55;
    --forest-light: #e6d98a;
    --forest-glow: #f1c46a;
    --river-trees: #4f6a3a;
    --river-mist: #c9ced0;
    --river-water: #9aa3a6;
    --river-rock: #6f6457;
  }
  html, body {
    margin: 0;
    padding: 0;
    width: 1200px;
    height: 857px;
    overflow: hidden;
    background: var(--stage);
  }
  .stage {
    position: relative;
    width: 1200px;
    height: 857px;
  }
  .banner {
    position: absolute;
    top: 216px;
    width: 461px;
    height: 383px;
    background: var(--paper);
    overflow: hidden;
  }
  .banner--listen { left: 133px; }
  .banner--create { left: 630px; }

  .banner__photo {
    position: absolute;
    left: 0;
    top: 0;
    height: 100%;
  }
  .banner__photo--forest {
    width: 190px;
    background:
      linear-gradient(90deg, rgba(255,255,255,0) 45%, var(--paper) 100%),
      linear-gradient(160deg, var(--forest-light) 0%, var(--forest-mid) 30%, var(--forest-deep) 55%, var(--forest-mid) 75%, var(--forest-glow) 100%);
  }
  .banner__photo--river {
    width: 230px;
    background:
      linear-gradient(90deg, rgba(255,255,255,0) 40%, var(--paper) 100%),
      linear-gradient(180deg, var(--river-trees) 0%, var(--river-trees) 28%, var(--river-mist) 45%, var(--river-water) 65%, var(--river-rock) 82%, var(--river-water) 100%);
  }
  .banner__photo--river::after {
    content: "";
    position: absolute;
    inset: 0;
    background: linear-gradient(180deg, rgba(255,255,255,0.85) 0%, rgba(255,255,255,0) 18%);
  }

  .banner__rings {
    position: absolute;
    left: 0;
    top: 0;
    width: 461px;
    height: 383px;
  }

  .banner__copy {
    position: absolute;
    top: 0;
    width: 260px;
    text-align: center;
    color: var(--ink);
    font-family: "EB Garamond", "Palatino Linotype", serif;
    font-style: italic;
  }
  .banner--listen .banner__copy { left: 170px; }
  .banner--create .banner__copy { left: 162px; width: 270px; }

  .banner__headline {
    margin: 0;
    position: absolute;
    left: 0;
    right: 0;
    top: 54px;
    font-size: 70px;
    font-weight: 400;
    line-height: 1;
  }
  .banner__tagline {
    margin: 0;
    position: absolute;
    left: 0;
    right: 0;
    top: 144px;
    font-size: 31px;
    line-height: 43px;
  }
  .banner__button {
    position: absolute;
    top: 272px;
    left: 50%;
    transform: translateX(-50%);
    width: 196px;
    height: 50px;
    box-sizing: border-box;
    border: 1.5px dashed var(--ink);
    border-radius: 12px;
    font-family: "Cinzel", "Trajan Pro", serif;
    font-style: normal;
    font-weight: 700;
    font-size: 23px;
    line-height: 48px;
    letter-spacing: 0.5px;
    color: var(--ink);
    text-decoration: none;
    white-space: nowrap;
  }
  .banner__url {
    position: absolute;
    left: -20px;
    right: -20px;
    top: 337px;
    font-size: 22px;
    margin: 0;
  }
</style>
</head>
<body>
<main class="stage">

  <section class="banner banner--listen">
    <div class="banner__photo banner__photo--forest" role="img" aria-label="Sunlit forest with rays of light through green trees"></div>
    <svg class="banner__rings" viewBox="0 0 461 383" aria-hidden="true">
      <g fill="none" stroke="var(--ring)" stroke-width="1.5">
        <circle cx="330" cy="300" r="50"/>
        <circle cx="330" cy="300" r="100"/>
        <circle cx="330" cy="300" r="150"/>
        <circle cx="330" cy="300" r="200"/>
      </g>
    </svg>
    <div class="banner__copy">
      <h2 class="banner__headline">Listen</h2>
      <p class="banner__tagline">online to<br>relaxing sounds</p>
      <a class="banner__button" href="http://www.vellora-tonebox.com/">LISTEN NOW</a>
      <p class="banner__url">www.vellora-tonebox.com</p>
    </div>
  </section>

  <section class="banner banner--create">
    <div class="banner__photo banner__photo--river" role="img" aria-label="Misty mountain river with rocks and forested bank"></div>
    <svg class="banner__rings" viewBox="0 0 461 383" aria-hidden="true">
      <g fill="none" stroke="var(--ring)" stroke-width="1.5">
        <circle cx="330" cy="300" r="50"/>
        <circle cx="330" cy="300" r="100"/>
        <circle cx="330" cy="300" r="150"/>
        <circle cx="330" cy="300" r="200"/>
      </g>
    </svg>
    <div class="banner__copy">
      <h2 class="banner__headline">Create</h2>
      <p class="banner__tagline">your own ambient<br>atmosphere</p>
      <a class="banner__button" href="http://www.vellora-tonebox.com/">LISTEN NOW</a>
      <p class="banner__url">www.vellora-tonebox.com</p>
    </div>
  </section>

</main>
</body>
</html>
```